Harlow Consulting, Business Cards for International Development Consultancy

I'm an independent consultant working in the international development sector. I work with small organisations in developing countries to help them develop their community based programs so that they can be internationally competitive. This means they need to work better with their own communities to deliver meaningful quality work and also improve the accountability of their work so that they can compete for international and domestic funding.

I like the idea of being a connector between community, local organisations and international best practice and back again (ie acknowledging that international best practice can learn a lot from community).

My surname is Harlow - so I'd like the logo to use the idea of web as a connector.

I work with people with sight impairments - would like my card to be useful for low vision (i.e. clear graphics, easy to read font) and no vision (i.e. brail).

Target Market(s)

international non-government organisations (i.e. corvane, lift the villages, brightpath aid), Blue Harbour Green Lantern, government (i.e. Australian Bureau of Overseas Partnerships, consulars), non government agencies,

Industry/Entity Type

Business

Contact Information for Business Card

International Development Consultant
Connecting International Development with Community

Mirela Harlow
Lead Consultant
Phone: +61 412 558127
Email: mharlow.consulting@quillmail.net

Font styles to use
Sans Serif

Colors
eaf1f7
85acd3
d3a5cc
0456a4
a64599
0255a3

Requirements
Nice to have
• brail
Should not have
• fancy fonts - needs to be easy to read.

```html
<!DOCTYPE html>
<html lang="en">
<head>
<meta charset="utf-8">
<title>Harlow Consulting – Business Cards</title>
<link rel="stylesheet" href="https://fonts.googleapis.com/css2?family=Open+Sans:wght@400;600;700&display=swap">
<style>
  :root {
    --brand-blue: #0456a4;
    --brand-blue-deep: #0255a3;
    --brand-blue-light: #85acd3;
    --brand-mist: #eaf1f7;
    --card-white: #ffffff;
    --stage: #dfe6ee;
    --ink-white: #ffffff;
  }
  * { box-sizing: border-box; margin: 0; padding: 0; }
  html, body { width: 1200px; height: 900px; overflow: hidden; }
  body {
    background: var(--stage);
    font-family: "Open Sans", Arial, sans-serif;
    display: flex;
    flex-direction: column;
    align-items: center;
    justify-content: space-evenly;
  }
  .card {
    position: relative;
    width: 630px;
    height: 360px;
    overflow: hidden;
    box-shadow: 0 8px 24px rgba(2, 40, 80, 0.22);
  }

  /* Back side */
  .card--back {
    background: linear-gradient(135deg, #1c6cb8 0%, var(--brand-blue) 45%, var(--brand-blue-deep) 100%);
    display: flex;
    align-items: center;
    justify-content: center;
  }
  .brand { text-align: center; }
  .brand__name {
    display: inline-flex;
    align-items: center;
    gap: 14px;
    font-weight: 600;
    font-size: 40px;
    line-height: 1;
    letter-spacing: 0.2px;
  }
  .brand__dot {
    width: 22px; height: 22px;
    border-radius: 50%;
    background: currentColor;
    flex: none;
  }
  .brand__tagline {
    margin-top: 8px;
    font-size: 16px;
    font-weight: 400;
  }
  .card--back .brand__name { color: var(--ink-white); }
  .card--back .brand__tagline { color: var(--brand-blue-light); }

  /* Front side */
  .card--front { background: var(--card-white); }
  .card--front .brand {
    position: absolute;
    top: 78px; left: 0; right: 0;
  }
  .card--front .brand__name { color: var(--brand-blue); font-size: 38px; }
  .card--front .brand__tagline { color: var(--brand-blue-light); }
  .front-wave {
    position: absolute;
    left: 0; bottom: 0;
    width: 630px; height: 200px;
  }
  .contact {
    position: absolute;
    left: 0; right: 0; bottom: 26px;
    text-align: center;
    color: var(--ink-white);
    font-size: 17px;
    line-height: 1.55;
  }
  .contact__person { font-size: 18px; }
  .contact__name { font-weight: 700; font-size: 19px; }
  .contact__sep { margin: 0 6px; }
  .contact__row { display: inline-flex; align-items: center; gap: 6px; }
  .contact__row + .contact__row { margin-left: 12px; }
  .contact__icon { width: 15px; height: 15px; }
</style>
</head>
<body>

  <section class="card card--back" aria-label="Business card back">
    <div class="brand">
      <div class="brand__name"><span class="brand__dot"></span>Harlow Consulting</div>
      <div class="brand__tagline">International Development Consultancy</div>
    </div>
  </section>

  <section class="card card--front" aria-label="Business card front">
    <svg class="front-wave" viewBox="0 0 630 200" preserveAspectRatio="none" aria-hidden="true">
      <path d="M0 22 C180 -4 420 -6 630 58 L630 66 C420 6 180 10 0 32 Z" fill="#85acd3"/>
      <path d="M0 30 C180 8 420 6 630 64 L630 200 L0 200 Z" fill="#0456a4"/>
    </svg>

    <div class="brand">
      <div class="brand__name"><span class="brand__dot"></span>Harlow Consulting</div>
      <div class="brand__tagline">International Development Consultancy</div>
    </div>

    <div class="contact">
      <div class="contact__person"><span class="contact__name">Tomas Reid</span><span class="contact__sep">•</span>Manager</div>
      <div>
        <span class="contact__row">
          <svg class="contact__icon" viewBox="0 0 16 16" aria-hidden="true"><path d="M4 1.5 6.2 4 5 6.2c.9 1.9 2.4 3.4 4.3 4.3L11.5 9.3 14.5 11.5 13 14.5C7 14.5 1.5 9 1.5 3Z" fill="#fff"/></svg>
          123 555 0190
        </span>
        <span class="contact__row">
          <svg class="contact__icon" viewBox="0 0 16 16" aria-hidden="true"><g fill="none" stroke="#fff" stroke-width="1.3"><circle cx="8" cy="8" r="6.5"/><ellipse cx="8" cy="8" rx="2.8" ry="6.5"/><path d="M1.5 8h13M2.6 4.5h10.8M2.6 11.5h10.8"/></g></svg>
          www.tomasreid.net
        </span>
      </div>
      <div>@ tomasreid@quillmail.net</div>
    </div>
  </section>

</body>
</html>
```